Web Design Project

We need a website design for our marketing agency: loftwaveo.com.au

We want something that is eye-catching and will wow audiences, yet at the same time it cannot turn-off corporate clients. The website should be highly focused on conversions with numerous call to actions on each page.

We like blue as our primary colour and have a mascot (the spider on the current website)

Target Market(s)

small business owners
small corporations
enterprise level business clients

Industry/Entity Type

Marketing

Requirements
Must have
• must incorporate the agency mascot (the spider on the website)

```html
<!DOCTYPE html>
<html lang="en">
<head>
<meta charset="utf-8">
<title>Loftwaveo – Digital Marketing</title>
<link href="https://fonts.googleapis.com/css2?family=Cinzel:wght@400;600&family=Open+Sans:wght@400;600&family=Arimo:wght@400;700&display=swap" rel="stylesheet">
<style>
:root{
  --blue-deep:#1f56c2;
  --blue:#3d7ee6;
  --blue-light:#6aa6f5;
  --sky:#6ec5f0;
  --navy:#0d4f86;
  --page:#ececec;
  --text:#555;
  --text-dark:#333;
  --white:#fff;
  --heading:#3b78db;
  --brace:#a9a9a9;
}
*{margin:0;padding:0;box-sizing:border-box}
html,body{width:993px;height:1200px;overflow:hidden}
body{position:relative;background:var(--page);font-family:Arimo,Arial,sans-serif;color:var(--text);font-size:10px}
.abs{position:absolute}
.header-band{left:0;top:0;width:993px;height:153px;background:linear-gradient(#6ea9f4,#2e69d4 70%,#1d55c0);border-bottom:4px solid #fff}
.top-links{right:85px;top:5px;color:#fff;font-size:10px;word-spacing:2px}
.top-links span{margin:0 4px}
.brand{left:99px;top:32px;display:flex;align-items:center;gap:10px}
.brand-dot{width:44px;height:44px;border-radius:50%;background:#cfd8e4}
.brand-name{font-family:'Open Sans',sans-serif;font-size:40px;color:#fff;letter-spacing:1px;font-weight:400}
.nav{left:497px;top:81px;display:flex;gap:10px}
.nav a{display:block;width:74px;height:32px;line-height:28px;border-radius:14px;background:linear-gradient(#fff,#d6d6d6);text-align:center;font-family:'Open Sans',sans-serif;font-size:10px;font-weight:600;color:#444;text-decoration:none;border:2px solid #e8e8e8}
.nav a.active{background:linear-gradient(#666,#222);color:#fff;border-color:#bbb}
.hero{left:94px;top:125px;width:806px;height:281px;background:#fff;box-shadow:0 12px 10px -8px rgba(0,0,0,.35)}
.hero-inner{left:6px;top:5px;width:795px;height:270px;background:linear-gradient(90deg,#e6e6e6,#f3f3f3);border:1px solid #ccc;overflow:hidden}
.hero-title{left:25px;top:38px;font-family:Cinzel,serif;font-size:20px;color:#4b8ae9;font-weight:600;line-height:29px;letter-spacing:.5px}
.hero-title span{display:block;padding-left:146px}
.hero-rule{left:28px;top:112px;width:320px;border-top:1px dotted #3b6fd0}
.hero-copy{left:13px;top:133px;width:320px;font-size:9.5px;line-height:15px;color:#888;letter-spacing:.3px}
.hero-copy b{color:#777}
.hero-photo{left:390px;top:0;width:404px;height:268px;background:linear-gradient(90deg,rgba(238,238,238,0),#d8dde4 18%,#b9c2cf 60%,#8895a6)}
.hero-brace{left:340px;top:50px;z-index:2}
.feature{top:433px;width:268px;height:185px;color:#fff;padding:10px 28px 10px 19px;box-shadow:0 14px 10px -10px rgba(0,0,0,.45)}
.feature h2{font-family:'Open Sans',sans-serif;font-weight:600;font-size:19px;margin:0 0 10px 0}
.feature p{font-size:10px;font-weight:700;line-height:20px}
.feature p.note{font-weight:400}
.feature .arrow{display:inline-block;width:0;height:0;border-left:4px solid #fff;border-top:3px solid transparent;border-bottom:3px solid transparent;margin:0 6px 0 3px}
.f1{left:93px;background:linear-gradient(160deg,#3a7fc0,#16548e 60%,#0f416f)}
.f2{left:364px;background:linear-gradient(160deg,#3bb0ea,#1a82c9 60%,#0e63a8)}
.f3{left:636px;background:linear-gradient(160deg,#66d8f6,#2cb0e3 60%,#0e8fcf)}
.about-title{left:103px;top:648px;font-family:'Open Sans',sans-serif;font-size:20px;font-weight:600;color:var(--heading)}
.about-copy{left:102px;top:680px;width:528px;font-size:9.5px;line-height:16.5px;color:#555;text-align:justify;letter-spacing:.2px}
.about-copy b{color:var(--text-dark)}
.about-copy p+p{margin-top:16px}
.btn{display:block;height:18px;line-height:18px;border-radius:9px;background:linear-gradient(#5c9cf5,#2b6cdc);color:#fff;font-size:10px;text-align:center}
.about-more{left:556px;top:843px;width:76px}
.contact{left:664px;top:653px;width:216px;height:230px;background:#fff}
.contact h3{height:23px;line-height:23px;background:linear-gradient(#5d9bf2,#2b68d6);color:#fff;text-align:center;font-family:'Open Sans',sans-serif;font-weight:400;font-size:14px;border-radius:6px 6px 0 0}
.row{position:absolute;left:0;width:216px;font-size:9.5px;color:#666;letter-spacing:.5px}
.row label{position:absolute;right:156px;top:3px}
.row i{position:absolute;left:71px;width:122px;height:17px;border:1px solid #ccc;border-radius:8px}
.row.msg i{left:74px;width:125px;height:58px;border-radius:6px}
.send{left:116px;top:195px;width:76px}
.divider{left:92px;top:904px;width:803px;border-top:1px dotted #999}
.col{top:916px;width:160px}
.col h4{height:24px;line-height:24px;background:linear-gradient(#5d9bf2,#2b68d6);color:#fff;font-family:'Open Sans',sans-serif;font-weight:400;font-size:14px;padding-left:25px;clip-path:polygon(0 0,94% 0,100% 60%,100% 100%,0 100%)}
.col .thumb{margin-top:12px;height:68px;border:1px solid #ccc;background:#fff;padding:4px}
.col .thumb div{width:100%;height:100%}
.col p{margin-top:10px;font-size:9px;line-height:15px;letter-spacing:-.1px;text-align:justify;color:#555;height:60px;overflow:hidden;padding:0 2px}
.col p b{color:#333}
.col .btn{margin:9px 0 0 auto;width:76px}
.vsep{top:916px;height:185px;border-left:1px dotted #999}
.footer{left:0;top:1129px;width:993px;height:71px;background:linear-gradient(#6aa6f5,#2a63d1);color:#fff;text-align:center}
.footer nav{margin-top:18px;font-size:10px;word-spacing:2px}
.footer nav span{margin:0 7px}
.footer small{display:block;margin-top:16px;font-size:11px}
</style>
</head>
<body>
<div class="abs header-band"></div>
<div class="abs top-links">Home<span>|</span>Contact Us<span>|</span>Login<span>|</span>Register</div>
<div class="abs brand"><span class="brand-dot"></span><span class="brand-name">LOFTWAVEO</span></div>
<nav class="abs nav"><a class="active">ABOUT US</a><a>SERVICES</a><a>BLOG</a><a>SEO PRICING</a><a>SEM</a></nav>

<section class="abs hero">
  <div class="abs hero-inner">
    <h1 class="abs hero-title">HIGH ROI DIGITAL<span>MARKETING.</span></h1>
    <div class="abs hero-rule"></div>
    <p class="abs hero-copy"><b>Lorem Ipsum is simply dummy</b> text of the printing and typesetting industry. Lorem Ipsum has been the industry's standard dummy text ever since the 1500s, when an unknown printer took a galley of type and scrambled it to make a type specimen book.</p>
    <div class="abs hero-photo" role="img" aria-label="Photo of two businessmen reviewing documents at a laptop"></div>
    <svg class="abs hero-brace" width="40" height="126" viewBox="0 0 40 126"><path d="M2 3 C22 3 18 20 20 40 C22 56 26 61 37 63 C26 65 22 70 20 86 C18 106 22 123 2 123" fill="none" stroke="var(--brace)" stroke-width="3.5" stroke-linecap="round"/></svg>
  </div>
</section>

<section class="abs feature f1">
  <h2>Online Ad Management</h2>
  <p>Need highly targeted traffic right now? Then let us help!</p>
  <p class="note"><span class="arrow"></span>We have a whole range of online advertising solutions</p>
  <p class="note"><span class="arrow"></span>we can handle everything and get you the highest ROI for your ad dollar.</p>
</section>
<section class="abs feature f2">
  <h2>Social Media</h2>
  <p>we can handle everything and get you the highest ROI for your ad dollar.</p>
  <p class="note"><span class="arrow"></span>We offer high quality SEO packages at competitive rates with GUARANTEED results.</p>
  <p class="note"><span class="arrow"></span>Whether you're a local business or a national enterprise, we can help your business grow.</p>
</section>
<section class="abs feature f3">
  <h2>SEO Packages</h2>
  <p>Want build your brand to create a loyal base of supporters for your business?</p>
  <p class="note"><span class="arrow"></span>We can advise which social media options are right for your business</p>
  <p class="note"><span class="arrow"></span>there are way more options than just Chatterly and Pingly !</p>
</section>

<h2 class="abs about-title">About US</h2>
<div class="abs about-copy">
  <p><b>Loftwaveo is run by Ethan Calder who resides in Brisbane, Australia. Ethan and his specialist team of marketing experts are here to help you build your</b> presence online. We have team members specializing in a range of fields such as: search engine optimisation, social media, online advertising, public relations, general marketing and copy writing. We can even overhaul and optimise your whole website.</p>
  <p><b>We are an internet marketing consultancy that understands how to effectively combine a diverse array of online marketing techniques to meet your unique needs. We c</b>an do much more than just increase your web traffic – we can help you get (and hold onto!) the attention of your target audience and can build your brand online.do much more than just increase your web traffic – we can help you get (and hold onto!) the attention of your target audience and can build your brand online.</p>
</div>
<a class="abs btn about-more">Read more..</a>

<aside class="abs contact">
  <h3>Contact Us</h3>
  <div class="row" style="top:37px"><label>Name :</label><i></i></div>
  <div class="row" style="top:58px"><label>Email :</label><i></i></div>
  <div class="row" style="top:79px"><label>Mobile :</label><i></i></div>
  <div class="row" style="top:101px"><label>Website :</label><i></i></div>
  <div class="row msg" style="top:122px"><label>Message :</label><i></i></div>
  <a class="abs btn send">Send</a>
</aside>

<div class="abs divider"></div>

<article class="abs col" style="left:105px">
  <h4>SEO Services</h4>
  <div class="thumb"><div role="img" aria-label="Illustration of colourful SEO keyword tiles" style="background:linear-gradient(135deg,#9bd0f0,#3a7fd0 50%,#f2a0b8)"></div></div>
  <p><b>It's not just about quantity of traffic but quality.</b> Loftwaveo's SEO services can drive targeted traffic to your site maximizing your visibility and</p>
  <a class="btn">Read more..</a>
</article>
<div class="abs vsep" style="left:289px"></div>
<article class="abs col" style="left:311px">
  <h4>Digital Marketing</h4>
  <div class="thumb"><div role="img" aria-label="Image of marketing words on a dark blue background" style="background:linear-gradient(135deg,#0d2a55,#1f63b5 50%,#0a1f40)"></div></div>
  <p><b>It's not just about quantity of traffic but quality.</b> Loftwaveo's SEO services can drive targeted traffic to your site maximizing your visibility and</p>
  <a class="btn">Read more..</a>
</article>
<div class="abs vsep" style="left:495px"></div>
<article class="abs col" style="left:519px">
  <h4>SEM Services</h4>
  <div class="thumb"><div role="img" aria-label="Image of internet marketing keys on a keyboard" style="background:linear-gradient(135deg,#e6e9ee,#7fb2e0 45%,#f0a860)"></div></div>
  <p><b>It's not just about quantity of traffic but quality.</b> Loftwaveo's SEO services can drive targeted traffic to your site maximizing your visibility and</p>
  <a class="btn">Read more..</a>
</article>
<div class="abs vsep" style="left:700px"></div>
<article class="abs col" style="left:720px">
  <h4>Social Media</h4>
  <div class="thumb"><div role="img" aria-label="Image of social app icons on a phone screen" style="background:linear-gradient(135deg,#0b2f5c,#2a78c8 50%,#14406e)"></div></div>
  <p><b>It's not just about quantity of traffic but quality.</b> Loftwaveo's SEO services can drive targeted traffic to your site maximizing your visibility and</p>
  <a class="btn">Read more..</a>
</article>

<footer class="abs footer">
  <nav>Home<span>|</span>About Us<span>|</span>Services<span>|</span>SEO Pricing<span>|</span>Blog<span>|</span>SEM<span>|</span>Contact Us</nav>
  <small>© 2011 Loftwaveo.com - All rights reserved</small>
</footer>
</body>
</html>
```